Plastic Business Card for Bookkeeper

We are looking for a simple professional business card design to use for printing on thin frosted plastic (see-through) card stock. Logo and brand guideline documents are attached as well as a photo of our old business card, and another business card example that we like.

Target Market(s)

Small Business

Industry/Entity Type

Bookkeeper

Contact Information for Business Card

Harriet Olsen CPA
Chief Executive Bookkeeper
T. 03 5926 4417
M. 0438 761 205
E. harriet@pinecrestledger.com
W. www.pinecrestledger.com

Font styles to use
Sans Serif

Colors
6b449b
00a990

Requirements
Must have
• Stick with logo colors. Writing should be clear and easy to read and not too cramped together.
Nice to have
• Tag line for back of the card - 'Not your ordinary Bookkeeper'

```html
<!DOCTYPE html>
<html lang="en">
<head>
<meta charset="utf-8">
<title>Pinecrest Ledger – Business Card</title>
<link href="https://fonts.googleapis.com/css2?family=Roboto:wght@400;500;700&display=swap" rel="stylesheet">
<style>
  :root {
    --page-bg: #d9cfc0;
    --frost: #ece7de;
    --frost-edge: #f7f3ec;
    --teal: #17706c;
    --purple: #6b449b;
    --cream: #f1e4c4;
  }
  * { margin: 0; padding: 0; box-sizing: border-box; }
  html, body {
    width: 687px;
    height: 1200px;
    overflow: hidden;
    background: var(--page-bg);
    font-family: "Roboto", Arial, sans-serif;
  }
  .canvas { position: relative; width: 687px; height: 1200px; }
  .card {
    position: absolute;
    left: 86px;
    width: 542px;
    height: 295px;
    border-radius: 14px;
    overflow: hidden;
    background: var(--frost);
    border: 1px solid var(--frost-edge);
    box-shadow: 0 6px 18px rgba(60, 45, 30, 0.18);
  }
  .card--front { top: 167px; }
  .card--back { top: 767px; }
  .card__art { position: absolute; inset: 0; width: 100%; height: 100%; }

  .brand {
    position: absolute;
    width: 200px;
    text-align: center;
    color: var(--purple);
    font-weight: 500;
    font-size: 17px;
    line-height: 24px;
    letter-spacing: 0.08em;
    text-transform: uppercase;
  }
  .card--front .brand { left: 21px; top: 122px; }
  .card--back .brand { left: 322px; top: 124px; }

  .contact {
    position: absolute;
    right: 27px;
    top: 149px;
    text-align: right;
    color: var(--cream);
  }
  .contact__name { font-size: 19px; font-weight: 500; line-height: 22px; }
  .contact__title { font-size: 13.5px; margin-top: 1px; }
  .contact__list {
    list-style: none;
    margin-top: 10px;
    font-size: 13px;
    line-height: 18px;
  }
  .contact__item {
    display: flex;
    justify-content: flex-end;
    align-items: center;
    gap: 9px;
  }
  .contact__icon { width: 9px; height: 9px; flex: none; }

  .tagline {
    position: absolute;
    left: 30px;
    bottom: 24px;
    color: var(--cream);
    font-size: 17px;
    font-weight: 500;
  }
</style>
</head>
<body>
<main class="canvas">

  <section class="card card--front" aria-label="Card front">
    <svg class="card__art" viewBox="0 0 542 295" aria-hidden="true">
      <path d="M372 0 C366 160 250 262 50 295 L542 295 L542 0 Z" fill="var(--teal)"/>
      <path d="M60 292 C210 258 345 170 356 10" fill="none" stroke="var(--purple)" stroke-width="3.5" stroke-linecap="round"/>
    </svg>

    <p class="brand">Pinecrest<br>Ledger</p>

    <div class="contact">
      <p class="contact__name">Harriet Olsen CPA</p>
      <p class="contact__title">Chief Executive Bookkeeper</p>
      <ul class="contact__list">
        <li class="contact__item">03 5926 4417
          <svg class="contact__icon" viewBox="0 0 10 10"><path d="M2 1 L4 1 L4.5 3 L3.3 3.8 C3.8 5 5 6.2 6.2 6.7 L7 5.5 L9 6 L9 8 C9 8.6 8.6 9 8 9 C4 9 1 6 1 2 C1 1.4 1.4 1 2 1 Z" fill="var(--cream)"/></svg>
        </li>
        <li class="contact__item">0438 761 205
          <svg class="contact__icon" viewBox="0 0 10 10"><rect x="2.5" y="0.8" width="5" height="8.4" rx="1" fill="none" stroke="var(--cream)" stroke-width="1.2"/><circle cx="5" cy="7.6" r="0.6" fill="var(--cream)"/></svg>
        </li>
        <li class="contact__item">harriet@pinecrestledger.com
          <svg class="contact__icon" viewBox="0 0 10 10"><rect x="0.8" y="2" width="8.4" height="6" rx="0.8" fill="none" stroke="var(--cream)" stroke-width="1.1"/><path d="M1 2.5 L5 5.5 L9 2.5" fill="none" stroke="var(--cream)" stroke-width="1.1"/></svg>
        </li>
        <li class="contact__item">www.pinecrestledger.com
          <svg class="contact__icon" viewBox="0 0 10 10"><circle cx="5" cy="5" r="4.2" fill="none" stroke="var(--cream)" stroke-width="1"/><ellipse cx="5" cy="5" rx="1.8" ry="4.2" fill="none" stroke="var(--cream)" stroke-width="0.8"/><path d="M0.8 5 H9.2" stroke="var(--cream)" stroke-width="0.8"/></svg>
        </li>
      </ul>
    </div>
  </section>

  <section class="card card--back" aria-label="Card back">
    <svg class="card__art" viewBox="0 0 542 295" aria-hidden="true">
      <path d="M0 0 L176 0 C182 160 300 262 480 295 L0 295 Z" fill="var(--teal)"/>
      <path d="M490 292 C330 262 204 172 196 10" fill="none" stroke="var(--purple)" stroke-width="3.5" stroke-linecap="round"/>
    </svg>

    <p class="brand">Pinecrest<br>Ledger</p>

    <p class="tagline">Not your ordinary Bookkeeper</p>
  </section>

</main>
</body>
</html>
```